Marta Belle Designs & Events business card

I need an elegant informative but not busy business card using my logo. We are a florist with high end customers. I am adding a PDF file and a PNG file for those who requested it
Updates

Target Market(s)

Brides, grooms, men purchasing flowers
Ages 20-65

Industry/Entity Type

Florist

Requirements
Must have
• Business info:
Marta Belle Design & Events
www.martabelleevents-sample.com.
555-418-2763

555-418-2763
Nice to have
• Est 1954
may want Pinterest logo, twitter and linkedin and facbook
Should not have
• Clip art or photos

```html
<!DOCTYPE html>
<html lang="en">
<head>
<meta charset="utf-8">
<title>Marta Belle Designs &amp; Events – Business Card</title>
<link rel="stylesheet" href="https://fonts.googleapis.com/css2?family=Cinzel:wght@400&family=Barlow:wght@500&family=EB+Garamond:wght@400&display=swap">
<style>
  :root {
    --page: #ffffff;
    --ink: #111111;
    --rose: #f2a9b8;
    --rose-text: #f4b6c3;
    --blush: #fbe8ec;
    --fold: #f6d3da;
    --edge: #3a3a3a;
  }
  * { box-sizing: border-box; margin: 0; padding: 0; }
  html, body {
    width: 1200px; height: 686px; overflow: hidden;
    background: var(--page);
  }
  .canvas { position: relative; width: 1200px; height: 686px; }

  .card { position: absolute; background: var(--page); border: 1.5px solid var(--edge); overflow: hidden; }

  /* Front – landscape */
  .card--front { left: 31px; top: 145px; width: 634px; height: 418px; }
  .brand-mark {
    position: absolute; left: 50%; transform: translateX(-50%);
    display: flex; align-items: center; justify-content: center;
    border: 2px solid var(--rose); border-radius: 50%;
  }
  .brand-mark__name {
    font-family: "Cinzel", serif; font-weight: 400; color: var(--rose);
    text-align: center; line-height: 1.2;
  }
  .card--front .brand-mark { top: 66px; width: 156px; height: 156px; }
  .card--front .brand-mark__name { font-size: 17px; }

  .wordmark {
    position: absolute; left: 0; right: 0; top: 246px; text-align: center;
    font-family: "Cinzel", serif; font-weight: 400; color: var(--ink);
    font-size: 58px; letter-spacing: 9px; line-height: 1;
  }
  .tagline {
    position: absolute; left: 0; right: 0; top: 330px; text-align: center;
    font-family: "Barlow", sans-serif; font-weight: 500; color: var(--rose);
    font-size: 17px; letter-spacing: 7.5px; line-height: 1;
  }

  /* Back – portrait */
  .card--back { left: 708px; top: 42px; width: 434px; height: 642px; background: var(--blush); }
  .back-shape { position: absolute; inset: 0; width: 100%; height: 100%; }
  .card--back .brand-mark { top: 216px; width: 150px; height: 150px; }
  .card--back .brand-mark__name { font-size: 16px; }
  .established {
    position: absolute; left: 0; right: 0; top: 380px; text-align: center;
    font-family: "EB Garamond", serif; color: var(--ink); font-size: 11px;
  }
  .contact {
    position: absolute; left: 27px; top: 530px; list-style: none;
    font-family: "EB Garamond", serif; color: var(--rose-text);
    font-size: 18px; line-height: 28.5px;
  }
</style>
</head>
<body>
<main class="canvas">

  <section class="card card--front" aria-label="Card front">
    <div class="brand-mark"><span class="brand-mark__name">Marta<br>Belle</span></div>
    <h1 class="wordmark">Marta Belle</h1>
    <p class="tagline">DESIGNS &amp; EVENTS</p>
  </section>

  <section class="card card--back" aria-label="Card back">
    <svg class="back-shape" viewBox="0 0 434 642" aria-hidden="true">
      <line x1="217" y1="0" x2="217" y2="100" stroke="var(--fold)" stroke-width="1.5"/>
      <path fill="var(--page)" d="M0 642 L0 190 C20 90 70 42 117 42 C170 42 205 70 217 100 C229 70 264 42 317 42 C364 42 414 90 434 190 L434 642 Z"/>
    </svg>
    <div class="brand-mark"><span class="brand-mark__name">Marta<br>Belle</span></div>
    <p class="established">Est 1954</p>
    <ul class="contact">
      <li>Marta Belle Design &amp; Events</li>
      <li>www.martabelleevents-sample.com.</li>
      <li>555-418-2763</li>
    </ul>
  </section>

</main>
</body>
</html>
```